Brightwave Audiology Letterhead redesign project

We need a full redesign of our current letterhead to make it consistent with the look and feel of our website design www.brightwaveaudio.com.au. It will need to include all information on the current version attached. The letterhead is used for sending medical reports and general correspondence. It should make use of our corporate colours (purple and teal) as per the logo on the existing file. The letterhead should be bold and eye-catching.

Target Market(s)

Medical practitioners.

Font styles to use
Sans Serif

Requirements
Must have
• It will need to include all information on the current version. Must have a premium, professional, high-end look and feel.
Nice to have
• Bold and eye-catching letterhead that reinforces the Brightwave Audiology brand. To stand out from other traditional letterheads.
Should not have
• The design should not be too cluttered or 'busy'

```html
<!DOCTYPE html>
<html lang="en">
<head>
<meta charset="utf-8">
<title>Brightwave Audiology Letterhead</title>
<link href="https://fonts.googleapis.com/css2?family=Arimo:wght@400;700&family=Carlito:ital,wght@0,400;0,700;1,400&display=swap" rel="stylesheet">
<style>
:root{
  --purple:#6a2c85;
  --teal:#1db584;
  --ink:#1a1a1a;
  --grey:#d6d6d6;
  --paper:#ffffff;
}
*{margin:0;padding:0;box-sizing:border-box}
html,body{width:1200px;height:1200px;overflow:hidden;background:var(--paper)}
.letterhead{position:relative;width:1200px;height:1200px;background:var(--paper);font-family:'Carlito',Calibri,sans-serif;color:var(--ink)}
.page{position:absolute;left:178px;top:0;width:846px;height:1200px;background:#fefefe}
.brand-name{position:absolute;left:84px;top:70px;width:230px;font-family:'Arimo',Arial,sans-serif;font-weight:700;font-size:30px;line-height:36px;color:var(--purple)}
.brand-dot{position:absolute;left:84px;top:42px;width:20px;height:20px;border-radius:50%;background:var(--teal)}
.divider{position:absolute;left:310px;top:32px;width:4px;height:150px;background:var(--grey)}
.contact{position:absolute;left:338px;font-family:'Arimo',Arial,sans-serif;font-size:17px;color:var(--ink);display:flex;align-items:center;gap:10px}
.contact svg{width:22px;height:22px;fill:var(--teal)}
.contact.web{font-size:20px;font-weight:700;color:var(--purple)}
.contact.web svg{fill:none;stroke:var(--purple);stroke-width:1.6}
.band-top{position:absolute;top:190px;height:13px}
.band-purple{left:0;width:312px;background:var(--purple)}
.band-teal{left:312px;width:534px;background:var(--teal)}
.photo-wash{position:absolute;left:0;top:440px;width:846px;height:665px;background:radial-gradient(ellipse 45% 55% at 48% 40%,rgba(200,190,185,.28),rgba(230,225,222,.12) 60%,rgba(255,255,255,0) 100%)}
.report-title{position:absolute;left:0;width:846px;top:272px;text-align:center;font-weight:700;font-size:19px;text-decoration:underline}
.report-body{position:absolute;left:68px;top:332px;width:690px;font-size:14.4px;line-height:28.7px}
.report-body p{margin-bottom:28.7px}
.sign-off{position:absolute;left:68px;top:966px;font-size:14.4px;line-height:22px}
.sign-off em{font-style:italic}
.band-foot-purple{position:absolute;left:0;top:1105px;width:846px;height:7px;background:var(--purple)}
.band-foot-teal{position:absolute;left:0;top:1112px;width:846px;height:5px;background:var(--teal)}
.badge{position:absolute;left:68px;top:1128px}
.clinicians{position:absolute;right:48px;top:1122px;text-align:right;font-family:'Arimo',Arial,sans-serif}
.clinicians .role{color:var(--teal);font-size:15px;font-weight:700;letter-spacing:.3px}
.clinicians .name{color:var(--purple);font-size:13px;line-height:16px}
.clinicians .name small{font-size:8.5px}
</style>
</head>
<body>
<div class="letterhead">
  <div class="page">
    <div class="photo-wash" role="img" aria-label="Faint background photo of a smiling child cupping hands behind ears"></div>

    <span class="brand-dot"></span>
    <div class="brand-name">Brightwave Audiology</div>
    <div class="divider"></div>

    <div class="contact" style="top:48px">
      <svg viewBox="0 0 24 24"><path d="M12 1a8 8 0 0 0-8 8c0 6 8 14 8 14s8-8 8-14a8 8 0 0 0-8-8zm0 11a3 3 0 1 1 0-6 3 3 0 0 1 0 6z"/></svg>
      48 Ridgeview Avenue, Kelmora, Qld 4361
    </div>
    <div class="contact" style="top:80px">
      <svg viewBox="0 0 24 24"><path d="M3 8c0-3 4-5 9-5s9 2 9 5v2h-5V8H8v2H3zM6 11h12l2 10H4z"/><circle cx="12" cy="16" r="2.5" fill="#fff"/></svg>
      07 5210 3344
      <svg viewBox="0 0 24 24" style="margin-left:14px"><rect x="2" y="3" width="6" height="19"/><rect x="9" y="8" width="13" height="14"/><rect x="11" y="10" width="9" height="3" fill="#fff"/></svg>
      07 5210 3345
    </div>
    <div class="contact" style="top:112px">
      <svg viewBox="0 0 24 24"><path d="M1 5h22v14H1z"/><path d="M1 5l11 8 11-8" fill="none" stroke="#fff" stroke-width="1.6"/></svg>
      hello@brightwaveaudio.com.au
    </div>
    <div class="contact web" style="top:156px">
      <svg viewBox="0 0 24 24"><circle cx="12" cy="12" r="10"/><ellipse cx="12" cy="12" rx="4.5" ry="10"/><path d="M2 12h20M4 7h16M4 17h16"/></svg>
      www.brightwaveaudio.com.au
    </div>

    <div class="band-top band-purple"></div>
    <div class="band-top band-teal"></div>

    <h1 class="report-title">REPORT</h1>

    <div class="report-body">
      <p>Lorem ipsum dolor sit amet, in dicunt hendrerit nam, vim ubique utamur ex, ex explicari scripserit temporibus pro. Cu eros nemore patrioque eos, nostro urbanitas ne nec. Nemore appellantur an mel, quo regione probatus signiferumque ei. Sit iriure insolens disputationi eu, vel causae expetenda omittantur ex. In adhuc solum sit, case veri voluptua pro ut.</p>
      <p>Sit veniam altera ea. Vix mundi feugiat euripidis et, vis essent scripta ne, ei munere temporibus concludaturque mei. Omnium concludaturque ad vis, ne qui posse percipit. Vim id iudicabit liberavisse, vim ne assum omnium malorum, vim eius consequat consequuntur ut. Nec idque eripuit ne, cu mei audiam invidunt, ad quot ornatus per. Ut sed tollit saperet salutatus, et sea malis omnes.</p>
      <p>Est prodesset constituto cu, amet affert senserit sit no. Maiorum platonem persecuti et vim. No nam inimicus suavitate. Ex agam solet feugait cum, dicunt graecis splendide vis an. Causae vivendum sensibus an ius, te cum esse appetere iracundia, vide ullum invenire mea ex.</p>
      <p>Animal senserit ne sed, nam ex nominati antiopam. Ne percipitur reformidans delicatissimi duo. Ut eruditi salutatus his, labitur salutatus eam ad, an usu putant lucilius. Has dictas scribentur at, id falli libris indoctum eam. Eruditi docendi albucius ne est.</p>
      <p>Tempor imperdiet in per, voluptua concludaturque duo no. Ea munere salutandi vix, vis impetus bonorum et, homero perfecto laboramus duo ut. Alii dictas tacimates te pro, posidonium ullamcorper et sea. Mei eu expetenda consequuntur mediocritatem, his admodum partiendo imperdiet id. Cu mei posse delicata.</p>
    </div>

    <div class="sign-off">
      Thank You<br>
      Sincerely,<br>
      <em>Brightwave Audiology</em>
    </div>

    <div class="band-foot-purple"></div>
    <div class="band-foot-teal"></div>

    <svg class="badge" width="150" height="44" viewBox="0 0 150 44" aria-label="Accreditation badge">
      <circle cx="18" cy="22" r="15" fill="none" stroke="#9bc94a" stroke-width="3"/>
      <rect x="40" y="10" width="100" height="10" rx="2" fill="#bdbdbd"/>
      <rect x="40" y="24" width="100" height="1.5" fill="#d0d0d0"/>
      <rect x="46" y="30" width="88" height="6" rx="2" fill="#e0e0e0"/>
    </svg>

    <div class="clinicians">
      <div class="role">CLINICAL AUDIOLOGISTS</div>
      <div class="name">DANIEL MARSH <small>BMUS, MAUDST, MAUDSA (CCP)</small></div>
      <div class="name">OWEN MARSH <small>BN, GRAD DIP FET, MAUDST, MAUDSA (CCP)</small></div>
    </div>
  </div>
</div>
</body>
</html>
```